Business Stationery - Business Cards - Letterheads, Compliment Slips

We need a new set of artwork designed for our client, they are a Construction Company, that also sell Kitchens, bathrooms and appliances.
They are an up and comping company that focus on quality and bespoke build. For them it is all about the quality of what they install, build or design. They have recently been awarded sole distributorship of a German kitchen brand Annelore Kuchen.
We need to present a quick job to them and provide some proofs for their new Artwork which encompasses all the elements of the company
The company name is the Halvorn Group and we need to design a logo also.
Any Questions please let me know asap

Target Market(s)
Upmarket clients, or small Development companies.
Industry/Entity Type
Business
Look and feel

```html
<!DOCTYPE html>
<html lang="en">
<head>
<meta charset="utf-8">
<title>Halvorn Group – Stationery</title>
<link href="https://fonts.googleapis.com/css2?family=EB+Garamond:wght@400&display=swap" rel="stylesheet">
<style>
  :root {
    --olive: #87904f;
    --olive-soft: #a7ab72;
    --olive-faint: #d5d9c0;
    --orange: #ee5a2c;
    --ink: #1a1a1a;
    --frame: #8c8c8c;
    --rule: #c9cba8;
    --paper: #ffffff;
  }
  * { margin: 0; padding: 0; box-sizing: border-box; }
  html, body { width: 1200px; height: 1200px; overflow: hidden; background: var(--paper); }
  body { position: relative; font-family: "EB Garamond", Garamond, serif; color: var(--ink); }

  .card-front, .card-back, .letterhead { position: absolute; }

  /* Business card – front */
  .card-front { left: 18px; top: 43px; width: 515px; height: 287px; border: 1px solid var(--frame); background: var(--paper); overflow: hidden; }
  .card-front .brand-block { position: absolute; left: 0; top: 0; width: 92px; height: 285px; background: var(--olive); }
  .card-front .brand-name { position: absolute; left: 116px; top: 30px; font-size: 38px; line-height: 1; color: var(--orange); }
  .card-front .holder { position: absolute; left: 242px; top: 118px; width: 150px; }
  .holder .name { font-size: 21px; color: var(--olive); line-height: 1.1; }
  .holder .position { font-size: 17px; color: var(--orange); line-height: 1.2; }
  .holder .divider { border-top: 1px solid var(--rule); margin: 12px 0 10px; }
  .holder .details { font-size: 16px; color: var(--olive); line-height: 21.5px; }

  /* Business card – back */
  .card-back { left: 18px; top: 363px; width: 515px; height: 286px; background: var(--olive); color: var(--paper); text-align: center; }
  .card-back .brand { position: absolute; left: 0; right: 0; top: 68px; display: flex; flex-direction: column; align-items: center; gap: 14px; }
  .card-back .brand-mark { width: 64px; height: 64px; background: var(--paper); }
  .card-back .brand-name { font-size: 36px; line-height: 1; }
  .card-back .web { position: absolute; left: 0; right: 0; top: 233px; font-size: 17px; }

  /* Letterhead */
  .letterhead { left: 545px; top: 43px; width: 621px; height: 1086px; border: 1px solid var(--frame); background: var(--paper); }
  .letterhead .brand-mark { position: absolute; left: 26px; top: 25px; width: 69px; height: 81px; background: var(--olive); color: var(--paper); font-size: 14px; line-height: 1.05; padding: 22px 4px 0 6px; }
  .letterhead .address { position: absolute; left: 101px; top: 41px; font-size: 10px; line-height: 14px; color: var(--olive-soft); padding-bottom: 2px; border-bottom: 1px solid var(--rule); }
  .letterhead .body { position: absolute; left: 60px; top: 232px; width: 498px; font-size: 19px; line-height: 24.2px; text-align: justify; hyphens: auto; }
  .letterhead .body p + p { margin-top: 24.2px; }
  .letterhead .sign-mark { position: absolute; left: 225px; top: 910px; display: flex; align-items: center; gap: 10px; }
  .sign-mark .square { width: 40px; height: 40px; background: var(--olive-faint); }
  .sign-mark .name { font-size: 26px; color: var(--olive-faint); }
  .letterhead .signature { position: absolute; right: 62px; top: 958px; text-align: right; font-size: 19px; line-height: 24.2px; }
</style>
</head>
<body>

<section class="card-front">
  <div class="brand-block"></div>
  <div class="brand-name">Halvorn Group</div>
  <div class="holder">
    <div class="name">Name Surname</div>
    <div class="position">position</div>
    <div class="divider"></div>
    <div class="details">lorem ipsum dolores<br>lorem ipsum dolores<br>lorem ipsum dolores</div>
  </div>
</section>

<section class="card-back">
  <div class="brand">
    <div class="brand-mark"></div>
    <div class="brand-name">Halvorn Group</div>
  </div>
  <div class="web">www.halvorngroup.com</div>
</section>

<section class="letterhead">
  <div class="brand-mark">Halvorn<br>Group</div>
  <div class="address">adress line goes here also contacts<br>adress line goes here also contacts</div>
  <div class="body" lang="la">
    <p>Lorem ipsum dolor sit amet, consectetur adipiscing elit. Donec orci purus, luctus vitae dignissim eu, iaculis sed purus. Vivamus faucibus, ipsum nec aliquet viverra, leo mauris condimentum ligula, sit amet sagittis enim ligula quis arcu. Nam egestas tortor id nisi porttitor mattis. In tortor ante, ultricies in suscipit a, tempus non massa. Vivamus et auctor mi. Fusce vel massa nulla. Phasellus nec eros mauris, et scelerisque orci. Donec malesuada orci vitae nulla accumsan porta a id massa. Quisque accumsan iaculis magna sit amet fringilla. Maecenas consequat, magna eget tincidunt semper, odio nibh rutrum mi, id feugiat ante nisi eu risus. Vestibulum nunc orci, rhoncus a placerat in, ultricies in mi. Cras mattis varius eros, vel fringilla nisi suscipit eget.</p>
    <p>Quisque scelerisque sagittis nulla at porttitor. Mauris a justo et tellus interdum tristique. Sed id augue vitae urna euismod commodo aliquet a quam. Pellentesque arcu velit, cursus et malesuada ut, consequat et diam. Nullam erat sem, rhoncus id ullamcorper vitae, rhoncus et arcu. In ultricies ultricies nulla, ut rutrum nisi iaculis at. Donec eu magna a metus ornare faucibus. Fusce aliquet faucibus ultricies. Morbi semper, est id tincidunt gravida, sem arcu adipiscing lacus, ac bibendum nulla leo eu purus. Quisque nec diam sed risus consectetur a ccumsan quis quis nibh. Vestibulum id purus lorem.</p>
  </div>
  <div class="sign-mark"><div class="square"></div><div class="name">Halvorn Group</div></div>
  <div class="signature">Name Surname<br>Co-Founder &amp; CEO</div>
</section>

</body>
</html>
```